The Quietness of Leaving Harbor Movie Poster

The Quietness of Leaving Harbor is a NCW (National Cinema Workshop) thesis short film. It's a story about a young marine coming home.

We need a movie poster design that goes to movie festivals.

Feel free to watch our cut. It's 9-min long. Pleas keep it confidential.
https://reelvault.net/948216037
password: 1502

Please meet the team on the web links below (one of them is active)
quietness-movie.pagebloom.net
http://thequietnessofleavingharbor.net

Target Market(s)

Major film festival programers

Industry/Entity Type

Film Production

Font styles to use
Other font styles liked:
• Font is TALL FILM To download at http://www.glyphbarn.net/font-comment.php?file=tall_films

Requirements
Must have
• Simple & clean design/visual
• Multiple design ideas
• I'd like to see different design ideas - perhaps one idea is design around a main imagery from the screen grab photos I provided among other ideas
Nice to have
• The movie is a slice of life.
• It might be nice to have the design that reflects the same tone

```html
<!DOCTYPE html>
<html lang="en">
<head>
<meta charset="utf-8">
<title>The Quietness of Leaving Harbor — Poster</title>
<link rel="stylesheet" href="https://fonts.googleapis.com/css2?family=Antonio:wght@700&family=Oswald:wght@400;500&display=swap">
<style>
  :root {
    --paper: #d9d0c0;
    --ink: #3a2a20;
    --ink-soft: #5a4a3e;
    --photo-dark: #1c1512;
    --photo-warm: #6b4a34;
    --photo-glow: #a88464;
  }
  html, body {
    margin: 0;
    padding: 0;
    width: 849px;
    height: 1200px;
    overflow: hidden;
    background: var(--paper);
  }
  .poster {
    position: relative;
    width: 849px;
    height: 1200px;
    background: var(--paper);
    overflow: hidden;
  }
  .key-still {
    position: absolute;
    top: 0;
    left: 0;
    width: 849px;
    height: 600px;
  }
  .tagline {
    position: absolute;
    top: 664px;
    left: 0;
    width: 849px;
    display: flex;
    align-items: center;
    justify-content: center;
    gap: 22px;
    font-family: "Oswald", sans-serif;
    font-weight: 500;
    font-size: 19px;
    letter-spacing: 3px;
    color: var(--ink);
  }
  .tagline .rule {
    width: 150px;
    height: 2px;
    background: var(--ink);
  }
  .title {
    position: absolute;
    top: 718px;
    left: 0;
    width: 849px;
    text-align: center;
    font-family: "Antonio", sans-serif;
    font-weight: 700;
    color: var(--ink);
    text-transform: uppercase;
    line-height: 1;
  }
  .title-main {
    position: relative;
    display: inline-block;
    font-size: 132px;
    letter-spacing: 1px;
    transform: scaleY(1.02);
  }
  .title-the {
    position: absolute;
    left: -30px;
    top: 4px;
    font-size: 19px;
    line-height: 0.95;
    width: 20px;
    text-align: center;
  }
  .title-sub {
    display: block;
    margin-top: 6px;
    font-size: 64px;
    letter-spacing: 1px;
  }
  .credits {
    position: absolute;
    top: 968px;
    left: 0;
    width: 849px;
    text-align: center;
    font-family: "Oswald", sans-serif;
    font-weight: 400;
    color: var(--ink-soft);
    font-size: 11px;
    letter-spacing: 1px;
    text-transform: uppercase;
    line-height: 22px;
  }
  .credits .role {
    font-size: 8px;
    margin-right: 5px;
  }
  .credits .entry {
    margin: 0 9px;
  }
</style>
</head>
<body>
<main class="poster">
  <svg class="key-still" viewBox="0 0 849 600" role="img" aria-label="Film still: a young marine seen from behind, greeted by a smiling older woman in a warmly lit room">
    <defs>
      <linearGradient id="still-tone" x1="0" y1="0" x2="1" y2="0.4">
        <stop offset="0" stop-color="var(--photo-glow)"/>
        <stop offset="0.35" stop-color="var(--photo-warm)"/>
        <stop offset="0.75" stop-color="var(--photo-dark)"/>
        <stop offset="1" stop-color="#120d0b"/>
      </linearGradient>
      <clipPath id="torn-edge">
        <polygon points="0,0 849,0 849,520 830,518 800,528 770,522 740,530 705,526 680,540 650,535 620,546 590,540 560,552 520,548 490,556 455,552 420,562 385,556 350,566 315,560 280,570 245,566 210,575 175,570 140,580 105,574 70,584 35,578 0,588"/>
      </clipPath>
    </defs>
    <rect width="849" height="600" fill="url(#still-tone)" clip-path="url(#torn-edge)"/>
  </svg>

  <div class="tagline">
    <span class="rule"></span>
    <span>AN NCW THESIS FILM</span>
    <span class="rule"></span>
  </div>

  <h1 class="title">
    <span class="title-main"><span class="title-the">T H E</span>Quietness</span>
    <span class="title-sub">of Leaving Harbor</span>
  </h1>

  <div class="credits">
    <div>
      <span class="entry"><span class="role">Producer</span>Mara Ellison</span>
      <span class="entry"><span class="role">Director</span>Devon Hartley</span>
      <span class="entry"><span class="role">Editor</span>Lena Vossberg</span>
    </div>
    <div>
      <span class="entry"><span class="role">Cinematographer</span>Otto Brandvik</span>
      <span class="entry"><span class="role">Production Designer</span>Clara Whitmore</span>
    </div>
  </div>
</main>
</body>
</html>
```